Wordpress Design - Accounting Practice Startup

We are a relatively new Accounting Firm in Sydney with a primary focus on the Not-For-Profit sector. We need a complete re-design of our wordpress based website: www.larkmoorledgers.com.au
We already have a logo design which we would like to keep using. See uploaded files.
We have a simple menu stucture:
- Home
- About Us
- Our Services
- Contact Us
(Suggestions welcome!)
Happy for it to be a single page scrolling website linked via the menu. We would like the "Our Services" page/section to have icons for the following:
- Bookkeeping
- Payroll
- Accounting
- Training
- Consulting
- Projects
We'd like a banner at the top of the page below the menu, and a place for testimonials, possibly integrated into the body or to the side. Images and icons to be included would be great.
Our main aim is to have an elegant and modern website that works well on all devices.
Industry/Entity Type
Accounting
Colors
Designer to choose colors to be used in the design.
Look and feel
Each slider illustrates characteristics of the customer's brand and the style your logo design should communicate.

```html
<!DOCTYPE html>
<html lang="en">
<head>
<meta charset="utf-8">
<title>Larkmoor Ledgers</title>
<link href="https://fonts.googleapis.com/css2?family=Poppins:wght@300;400;500;600&display=swap" rel="stylesheet">
<style>
:root{
  --green:#3aa33f;
  --green-dark:#2f8a34;
  --ink:#222;
  --text:#666;
  --muted:#888;
  --white:#fff;
  --dark:#2a2e32;
  --dark-line:#3c4146;
  --light:#eceeef;
  --field:#f4f4f4;
}
*{box-sizing:border-box;margin:0;padding:0}
html,body{width:1200px;height:2985px;overflow:hidden}
body{font-family:"Poppins",sans-serif;color:var(--ink);background:var(--light)}
.canvas{position:relative;width:1200px;height:2985px;overflow:hidden;background:linear-gradient(180deg,#f4f4f4 0,#e9e9e9 1400px,#eef0f2 1500px,#eef0f2 2300px)}
.abs{position:absolute}
.center{left:0;width:1200px;text-align:center}

/* hero */
.hero-bg{position:absolute;left:0;top:0}
.logo{position:absolute;left:155px;top:22px;display:flex;align-items:center;gap:12px}
.logo-square{width:26px;height:26px;background:var(--green)}
.logo-name{font-size:27px;font-weight:400;color:var(--white);line-height:28px;letter-spacing:.5px;width:200px}
.nav{position:absolute;top:40px;right:148px;display:flex;gap:38px;font-size:10px;letter-spacing:.6px}
.nav a{color:var(--white);text-decoration:none;text-transform:uppercase}
.nav a.active{color:var(--green)}
.quote-mark{position:absolute;left:230px;top:128px;font-size:60px;color:var(--white);font-weight:600;line-height:1}
.hero-text{position:absolute;left:232px;top:198px;width:420px;font-size:15px;line-height:24px;color:var(--white);font-weight:400}
.hero-name{position:absolute;left:232px;top:324px;color:var(--white);font-size:13px;font-weight:600}
.hero-role{position:absolute;left:232px;top:344px;color:#ddd;font-size:11px}
.btn{display:inline-flex;align-items:center;justify-content:center;font-size:10px;font-weight:500;letter-spacing:.8px;text-transform:uppercase;text-decoration:none}
.btn-light{position:absolute;left:232px;top:388px;width:128px;height:32px;background:var(--white);color:var(--ink)}
.slider-dots{position:absolute;left:936px;top:206px;display:flex;flex-direction:column;gap:9px}
.slider-dots span{width:13px;height:13px;border:2px solid var(--white);border-radius:50%}
.slider-dots span.on{background:var(--green);border-color:var(--green)}

/* headings */
.eyebrow{font-size:9px;letter-spacing:1.5px;color:#555;text-transform:uppercase}
.title{font-size:19px;font-weight:600;text-transform:uppercase;margin-top:4px}
.title em{font-style:normal;color:var(--green)}
.title-rule{width:36px;margin:6px auto 0;border-top:1px dashed #aaa}

/* about */
.about-text{position:absolute;left:260px;width:680px;top:640px;text-align:center;font-size:12.5px;line-height:20px;color:var(--text)}
.btn-green{background:var(--green);color:var(--white)}

/* team */
.team-card{position:absolute;top:928px;width:280px;height:318px;background:var(--white);box-shadow:0 2px 8px rgba(0,0,0,.12);border-bottom:4px solid #555;text-align:center}
.team-card.active{border-bottom-color:var(--green)}
.team-photo{margin:10px;height:210px;background:linear-gradient(160deg,#d8d8d8,#8a8a8a)}
.team-name{margin-top:22px;font-size:14px;font-weight:500}
.team-card.active .team-name{color:var(--green)}
.team-role{margin-top:4px;font-size:10.5px;color:var(--muted);letter-spacing:.6px;text-transform:uppercase}
.pager{position:absolute;top:1280px;left:0;width:1200px;display:flex;justify-content:center;gap:8px}
.pager span{width:13px;height:13px;border:1.5px solid #666;border-radius:50%}
.pager span.on{background:var(--green);border-color:var(--green)}
.btn-dark{position:absolute;left:520px;top:1326px;width:162px;height:30px;background:#333;color:var(--white)}

/* services */
.service{position:absolute;width:280px;height:300px;background:var(--white);box-shadow:0 2px 8px rgba(0,0,0,.1);border-bottom:4px solid #555;text-align:center}
.service.active{border-bottom-color:var(--green)}
.service-icon{position:absolute;left:70px;top:-40px;width:140px;height:140px}
.service h3{position:absolute;top:150px;width:100%;font-size:14px;font-weight:500}
.service p{position:absolute;top:186px;left:22px;right:22px;font-size:11.5px;line-height:18px;color:var(--text)}
.service .more{position:absolute;top:258px;left:0;width:100%;font-size:10px;letter-spacing:.8px;color:#333;text-transform:uppercase}
.service .more span{border-bottom:1px solid #333;padding-bottom:1px}
.service.active .more{color:var(--green)}
.service.active .more span{border-color:var(--green)}

/* contact */
.contact-bg{position:absolute;left:0;top:2250px;width:1200px;height:430px;background:linear-gradient(180deg,rgba(238,240,242,1) 0,rgba(200,205,210,.7) 45%,#a9b0b6 100%)}
.field{position:absolute;height:34px;background:var(--field);font-size:11px;color:#777;padding:9px 10px}
.btn-send{position:absolute;left:553px;top:2584px;width:94px;height:32px;background:var(--green);color:var(--white);gap:6px}

/* footer */
.footer{position:absolute;left:0;top:2680px;width:1200px;height:305px;background:var(--dark);color:var(--white)}
.foot-name{position:absolute;left:155px;top:48px;font-size:22px;font-weight:400;color:var(--white);line-height:26px;width:180px}
.foot-info{position:absolute;left:384px;top:50px;font-size:12px;line-height:18px;color:#ccc}
.foot-info b{color:var(--white);font-weight:600;font-size:13px}
.foot-info .link{text-decoration:underline}
.badge{position:absolute;top:46px;width:172px;height:120px;background:#3b4045}
.badge-mark{position:absolute;left:56px;top:30px;width:60px;height:60px;border-radius:50%;background:#555b61}
.foot-rule{position:absolute;left:135px;top:212px;width:930px;border-top:1px solid var(--dark-line)}
.copyright{position:absolute;left:155px;top:244px;font-size:10.5px;line-height:14px;color:#aaa}
.foot-nav{position:absolute;left:400px;top:250px;display:flex;gap:30px;font-size:10px;letter-spacing:.6px;text-transform:uppercase}
.foot-nav a{color:#ccc;text-decoration:none}
.foot-nav a.active{color:var(--green)}
.social{position:absolute;left:896px;top:244px;display:flex;gap:12px}
.social span{width:28px;height:28px;border:1px solid #777;border-radius:50%;display:flex;align-items:center;justify-content:center}
.social span.on{background:var(--green);border-color:var(--green)}
.social i{width:8px;height:8px;border-radius:50%;background:#ccc}
.social span.on i{background:var(--white)}
</style>
</head>
<body>
<div class="canvas">

  <!-- hero -->
  <svg class="hero-bg" width="1200" height="580" viewBox="0 0 1200 580" role="img" aria-label="Black and white photo of a desk with keyboard, phone and pen">
    <defs>
      <linearGradient id="heroGrad" x1="0" y1="0" x2="1" y2="1">
        <stop offset="0" stop-color="#9a9a9a"/>
        <stop offset=".5" stop-color="#6f6f6f"/>
        <stop offset="1" stop-color="#3f3f3f"/>
      </linearGradient>
    </defs>
    <polygon points="0,0 1200,0 1200,420 0,560" fill="url(#heroGrad)"/>
    <polygon points="0,190 1200,412 1200,432 0,560" fill="#3aa33f" opacity=".9"/>
    <polygon points="0,190 470,277 0,560" fill="#3aa33f"/>
    <polygon points="0,560 1200,432 1200,446 0,572" fill="#e3e3e3"/>
  </svg>

  <div class="logo">
    <span class="logo-square"></span>
    <span class="logo-name">LARKMOOR LEDGERS</span>
  </div>

  <nav class="nav">
    <a class="active" href="#home">- Home -</a>
    <a href="#about">About Us</a>
    <a href="#services">Our Services</a>
    <a href="#contact">Contact Us</a>
  </nav>

  <div class="quote-mark">&ldquo;</div>
  <p class="hero-text">Contrary to popular belief, Lorem Ipsum is not random text. It has roots in a piece of classical Latin literature from 45 BC, making it over 2000 years old, Tomas Verrill.</p>
  <div class="hero-name">Finibus</div>
  <div class="hero-role">Standard Chunk</div>
  <a class="btn btn-light" href="#contact">Contact Us</a>

  <div class="slider-dots"><span></span><span class="on"></span><span></span><span></span></div>
  <svg class="abs" style="left:914px;top:342px" width="44" height="24" viewBox="0 0 44 24">
    <polygon points="14,2 2,12 14,22" fill="#fff"/>
    <polygon points="26,2 40,12 26,22" fill="#3aa33f"/>
  </svg>

  <!-- about -->
  <div class="abs center" style="top:562px">
    <div class="eyebrow">About</div>
    <div class="title">Larkmoor <em>Ledgers</em></div>
    <div class="title-rule"></div>
  </div>
  <p class="about-text">Larkmoor Ledgers originated with the idea of providing accounting services that would make clients feel safe and find refuge, feel confident that they could trust the numbers in their financial reports. The founders of Larkmoor Ledgers migrated to Australia as refugees and the name of the business alludes to these origins. We strongly believe that every number counts...</p>
  <a class="btn btn-green abs" style="left:536px;top:752px;width:128px;height:32px" href="#about">Explore More</a>

  <!-- team -->
  <div class="abs center" style="top:848px">
    <div class="eyebrow">Who we are</div>
    <div class="title">Our <em>Team</em></div>
    <div class="title-rule"></div>
  </div>

  <svg class="abs" style="left:108px;top:1076px" width="22" height="24" viewBox="0 0 22 24"><polygon points="20,0 2,12 20,24 14,12" fill="#666"/></svg>
  <svg class="abs" style="left:1068px;top:1076px" width="22" height="24" viewBox="0 0 22 24"><polygon points="2,0 20,12 2,24 8,12" fill="#3aa33f"/></svg>

  <div class="team-card" style="left:157px">
    <div class="team-photo" role="img" aria-label="Portrait photo of the principal consultant"></div>
    <div class="team-name">Mira Castell</div>
    <div class="team-role">Principal Consultant</div>
  </div>
  <div class="team-card active" style="left:461px">
    <div class="team-photo" role="img" aria-label="Portrait photo of the consultant"></div>
    <div class="team-name">Owen Thale</div>
    <div class="team-role">Consultant</div>
  </div>
  <div class="team-card" style="left:765px">
    <div class="team-photo" role="img" aria-label="Portrait photo of a principal consultant"></div>
    <div class="team-name">Nunc ultricies</div>
    <div class="team-role">Principal Consultant</div>
  </div>

  <div class="pager"><span></span><span></span><span class="on"></span><span></span></div>
  <a class="btn btn-dark" href="#team">All Team Members</a>

  <svg class="abs" style="left:0;top:1370px" width="1200" height="130" viewBox="0 0 1200 130">
    <polygon points="0,112 1200,0 1200,22 0,120" fill="#4d5258"/>
    <polygon points="0,120 1200,22 1200,130 0,130" fill="#eef0f2"/>
  </svg>

  <!-- services -->
  <div class="abs center" style="top:1498px">
    <div class="eyebrow">What we do</div>
    <div class="title">Our <em>Services</em></div>
    <div class="title-rule"></div>
  </div>

  <div class="service" style="left:157px;top:1620px">
    <svg class="service-icon" viewBox="0 0 140 140"><circle cx="70" cy="70" r="68" fill="#fff" stroke="#3aa33f" stroke-width="1" stroke-dasharray="2 2"/><circle cx="70" cy="70" r="60" fill="#fff" stroke="#3aa33f" stroke-width="4"/>
      <g fill="none" stroke="#333" stroke-width="3"><rect x="46" y="44" width="40" height="50" rx="3"/><line x1="54" y1="56" x2="78" y2="56"/><line x1="54" y1="66" x2="72" y2="66"/><rect x="40" y="72" width="22" height="28" fill="#fff"/><circle cx="88" cy="76" r="11" fill="#fff"/></g>
      <text x="88" y="81" font-size="13" text-anchor="middle" fill="#333" font-family="Poppins,sans-serif">$</text></svg>
    <h3>Bookkeeping</h3>
    <p>Neque porro quisquam est qui dolo em ipsum quia dolor sit amet, consectetur...</p>
    <div class="more"><span>Continue Reading</span></div>
  </div>

  <div class="service active" style="left:461px;top:1620px">
    <svg class="service-icon" viewBox="0 0 140 140"><circle cx="70" cy="70" r="68" fill="#fff" stroke="#3aa33f" stroke-width="1" stroke-dasharray="2 2"/><circle cx="70" cy="70" r="62" fill="#3aa33f"/>
      <g fill="#3aa33f" stroke="#fff" stroke-width="3"><rect x="62" y="42" width="28" height="48"/><rect x="56" y="46" width="28" height="48"/><rect x="50" y="50" width="28" height="48"/></g>
      <text x="64" y="81" font-size="20" font-weight="600" text-anchor="middle" fill="#fff" font-family="Poppins,sans-serif">$</text></svg>
    <h3 style="color:var(--green)">Payroll</h3>
    <p>Neque porro quisquam est qui dolo em ipsum quia dolor sit amet, consectetur...</p>
    <div class="more"><span>Continue Reading</span></div>
  </div>

  <div class="service" style="left:765px;top:1620px">
    <svg class="service-icon" viewBox="0 0 140 140"><circle cx="70" cy="70" r="68" fill="#fff" stroke="#3aa33f" stroke-width="1" stroke-dasharray="2 2"/><circle cx="70" cy="70" r="60" fill="#fff" stroke="#3aa33f" stroke-width="4"/>
      <g fill="none" stroke="#333" stroke-width="3"><rect x="46" y="44" width="34" height="50" rx="3"/><rect x="56" y="40" width="14" height="8"/><rect x="70" y="64" width="24" height="32" fill="#fff"/><line x1="54" y1="60" x2="64" y2="60"/><line x1="54" y1="70" x2="62" y2="70"/><line x1="76" y1="74" x2="88" y2="74"/><line x1="76" y1="84" x2="88" y2="84"/></g></svg>
    <h3>Accounting</h3>
    <p>Neque porro quisquam est qui dolo em ipsum quia dolor sit amet, consectetur...</p>
    <div class="more"><span>Continue Reading</span></div>
  </div>

  <div class="service" style="left:157px;top:1990px">
    <svg class="service-icon" viewBox="0 0 140 140"><circle cx="70" cy="70" r="68" fill="#fff" stroke="#3aa33f" stroke-width="1" stroke-dasharray="2 2"/><circle cx="70" cy="70" r="60" fill="#fff" stroke="#3aa33f" stroke-width="4"/>
      <g fill="none" stroke="#333" stroke-width="3"><rect x="58" y="42" width="40" height="30"/><line x1="70" y1="72" x2="64" y2="96"/><line x1="86" y1="72" x2="92" y2="96"/><polyline points="64,64 74,54 80,60 90,50"/></g>
      <circle cx="48" cy="54" r="6" fill="#333"/><rect x="42" y="62" width="12" height="34" fill="#333"/></svg>
    <h3>Training</h3>
    <p>Neque porro quisquam est qui dolo em ipsum quia dolor sit amet, consectetur...</p>
    <div class="more"><span>Continue Reading</span></div>
  </div>

  <div class="service" style="left:461px;top:1990px">
    <svg class="service-icon" viewBox="0 0 140 140"><circle cx="70" cy="70" r="68" fill="#fff" stroke="#3aa33f" stroke-width="1" stroke-dasharray="2 2"/><circle cx="70" cy="70" r="60" fill="#fff" stroke="#3aa33f" stroke-width="4"/>
      <g fill="#333"><circle cx="70" cy="46" r="7"/><rect x="61" y="55" width="18" height="10" rx="4"/><circle cx="50" cy="78" r="7"/><rect x="41" y="87" width="18" height="10" rx="4"/><circle cx="90" cy="78" r="7"/><rect x="81" y="87" width="18" height="10" rx="4"/></g>
      <polyline points="50,68 70,66 90,68" fill="none" stroke="#333" stroke-width="2"/></svg>
    <h3>Support</h3>
    <p>Neque porro quisquam est qui dolo em ipsum quia dolor sit amet, consectetur...</p>
    <div class="more"><span>Continue Reading</span></div>
  </div>

  <div class="service" style="left:765px;top:1990px">
    <svg class="service-icon" viewBox="0 0 140 140"><circle cx="70" cy="70" r="68" fill="#fff" stroke="#3aa33f" stroke-width="1" stroke-dasharray="2 2"/><circle cx="70" cy="70" r="60" fill="#fff" stroke="#3aa33f" stroke-width="4"/>
      <g fill="none" stroke="#333" stroke-width="3"><rect x="44" y="44" width="44" height="36"/><rect x="52" y="52" width="44" height="36" fill="#fff"/><polyline points="58,80 68,70 76,76 88,62"/></g></svg>
    <h3>Projects</h3>
    <p>Neque porro quisquam est qui dolo em ipsum quia dolor sit amet, consectetur...</p>
    <div class="more"><span>Continue Reading</span></div>
  </div>

  <!-- contact -->
  <div class="contact-bg" role="img" aria-label="Faded photo of hands typing on a laptop keyboard"></div>
  <div class="abs center" style="top:2344px">
    <div class="eyebrow">Need help?</div>
    <div class="title">Contact <em>Us</em></div>
    <div class="title-rule"></div>
  </div>
  <div class="field" style="left:231px;top:2424px;width:236px">Name:</div>
  <div class="field" style="left:482px;top:2424px;width:236px">Email:</div>
  <div class="field" style="left:733px;top:2424px;width:236px">Phone:</div>
  <div class="field" style="left:231px;top:2476px;width:738px;height:86px">Message...</div>
  <a class="btn btn-send" href="#contact">
    <svg width="10" height="10" viewBox="0 0 10 10"><polygon points="0,4 10,0 6,10 5,6" fill="#fff"/></svg>Send
  </a>

  <!-- footer -->
  <footer class="footer">
    <div class="foot-name">LARKMOOR LEDGERS</div>
    <div class="foot-info">
      <b>Call Us:</b><br>
      0400 - 555 - 018<br>
      <span class="link">mira@larkmoorledgers.com.au</span><br><br>
      <b>Locations:</b><br>
      4410 Harbour View Rd,<br>
      Glenmore, NSW 2570
    </div>
    <div class="badge" style="left:688px"><span class="badge-mark"></span></div>
    <div class="badge" style="left:872px"><span class="badge-mark"></span></div>
    <svg class="abs" style="left:1122px;top:48px" width="26" height="20" viewBox="0 0 26 20"><polygon points="13,0 26,20 13,13 0,20" fill="#3aa33f"/></svg>
    <div class="foot-rule"></div>
    <div class="copyright">&copy; 2017 Larkmoor Ledgers.<br>All rights reserved.</div>
    <nav class="foot-nav">
      <a class="active" href="#home">- Home -</a>
      <a href="#about">About Us</a>
      <a href="#services">Our Services</a>
      <a href="#contact">Contact Us</a>
    </nav>
    <div class="social"><span><i></i></span><span class="on"><i></i></span><span><i></i></span><span><i></i></span></div>
  </footer>

</div>
</body>
</html>
```